Need Eye Catching For Sale By Owner Signs

In need of a Eye Catching For Sale By Owner Sign design. I plan on using the sign to market buildings and raw land that I own. The design should be able to scale to different rectangular dimensions for example a yard stake sign or a large 4' x 6' sign to be tacked to plywood. The design should have a dead space near the bottom that I can insert more detail information into at a later time.

The main tag line "For Sale By Owner" and the contact number "318-562-4097" needs to be easily be read from a distance.

```html
<!DOCTYPE html>
<html lang="en">
<head>
<meta charset="utf-8">
<title>For Sale By Owner Sign</title>
<link href="https://fonts.googleapis.com/css2?family=Carlito:wght@700&display=swap" rel="stylesheet">
<style>
  :root {
    --sign-blue: #4f25f0;
    --ink: #000000;
    --shadow: #555555;
    --panel: #ffffff;
    --page: #ffffff;
  }
  * { margin: 0; padding: 0; box-sizing: border-box; }
  html, body {
    width: 1200px;
    height: 893px;
    overflow: hidden;
    background: var(--page);
  }
  .sign {
    position: relative;
    width: 1200px;
    height: 893px;
    font-family: "Carlito", "Calibri", sans-serif;
    font-weight: 700;
    color: var(--ink);
  }
  .sign-board {
    position: absolute;
    left: 57px;
    top: 45px;
    width: 1097px;
    height: 805px;
    background: var(--sign-blue);
  }
  .headline {
    position: absolute;
    left: 0;
    width: 1200px;
    top: 40px;
    text-align: center;
    font-size: 290px;
    line-height: 1;
    letter-spacing: -2px;
    text-shadow: 6px 6px 0 var(--shadow);
    white-space: nowrap;
  }
  .phone-panel {
    position: absolute;
    left: 129px;
    top: 302px;
    width: 951px;
    height: 176px;
    background: var(--panel);
    border: 5px solid var(--ink);
    display: flex;
    align-items: center;
    justify-content: center;
  }
  .phone-number {
    font-size: 120px;
    line-height: 1;
    font-variant-numeric: oldstyle-nums;
    white-space: nowrap;
    margin-top: -8px;
  }
  .tagline {
    position: absolute;
    left: 0;
    width: 1200px;
    top: 481px;
    text-align: center;
    font-size: 132px;
    line-height: 1;
    white-space: nowrap;
  }
  .details-panel {
    position: absolute;
    left: 87px;
    top: 608px;
    width: 1040px;
    height: 207px;
    background: var(--panel);
    border: 5px solid var(--ink);
  }
</style>
</head>
<body>
  <main class="sign">
    <div class="sign-board"></div>
    <h1 class="headline">For Sale</h1>
    <div class="phone-panel">
      <p class="phone-number">318-562-4097</p>
    </div>
    <p class="tagline">BY OWNER</p>
    <div class="details-panel"></div>
  </main>
</body>
</html>
```